Content processing platform needs a new front page design

We need a new front page design for Textlyne.com. Textlyne.com is a free content processing platform that helps online businesses and freelancers scale their production of content and translation. See pdf for a mockup on what we wish to communicate and layout of the front page. The final design should communicate scalability/growth and we hope to see a design where the user clicks one of the links for iGaming, e-shop, agency in the middle. 60% of our traffic is from mobile devices..

```html
<!DOCTYPE html>
<html lang="en">
<head>
<meta charset="utf-8">
<title>Textlyne – Scale your content and translation</title>
<link rel="stylesheet" href="https://fonts.googleapis.com/css2?family=Open+Sans:ital,wght@0,400;0,600;0,700;1,400&display=swap">
<style>
:root{
  --blue:#1ba3e6;
  --blue-deep:#1776ad;
  --pink:#f0325a;
  --ink:#2d2f33;
  --muted:#6b6f75;
  --line:#e2e5e8;
  --paper:#ffffff;
  --mist:#f3f4f5;
  --night:#2a2b2d;
  --hero-a:#3a3b3e;
  --hero-b:#17181a;
}
*{box-sizing:border-box;margin:0;padding:0}
html,body{width:1200px;height:4018px;overflow:hidden}
body{font-family:"Open Sans",Arial,sans-serif;color:var(--ink);background:var(--paper);position:relative}
.wrap{position:absolute;left:0;width:1200px}
.accent{color:var(--blue)}
.section-title{font-size:20px;font-weight:600;letter-spacing:.5px;text-transform:uppercase;text-align:center;color:var(--ink)}

/* nav */
.nav{top:0;height:72px;background:var(--paper);border-bottom:1px solid var(--line)}
.brand{position:absolute;left:153px;top:22px;font-size:24px;font-weight:700;color:var(--blue);letter-spacing:-.3px}
.menu{position:absolute;left:402px;top:28px;display:flex;gap:24px;font-size:11px;font-weight:600;color:var(--ink)}
.menu .on{color:var(--blue)}
.nav-btn{position:absolute;top:20px;height:32px;border:1.5px solid var(--blue);border-radius:3px;color:var(--blue);font-size:10px;font-weight:700;line-height:29px;text-align:center}

/* hero */
.hero{top:72px;height:477px;background:linear-gradient(135deg,var(--hero-a),var(--hero-b))}
.hero h1{position:absolute;left:161px;top:120px;width:420px;font-size:26px;font-weight:400;line-height:36px;color:#fff}
.hero h1 b{font-weight:700}
.hero-col{position:absolute;top:228px;width:210px;color:#fff}
.hero-col h3{font-size:17px;font-weight:400;margin-bottom:14px}
.hero-col p{font-size:11px;line-height:17px;color:#d6d7d9;height:40px}
.cta{display:block;margin-top:12px;width:155px;height:28px;background:var(--pink);border-radius:3px;color:#fff;font-size:9px;font-weight:700;line-height:28px;text-align:center}
.video{position:absolute;left:622px;top:89px;width:262px;height:205px;background:linear-gradient(160deg,#eceeef,#c9ccd0);border-radius:8px;border:10px solid #f7f8f8}
.video-label{position:absolute;left:0;right:0;top:78px;text-align:center;color:#fff;font-size:11px}
.video-play{position:absolute;left:112px;top:42px}
.video-stand{position:absolute;left:716px;top:304px;width:74px;height:60px;background:linear-gradient(#e6e7e9,#bfc2c6);clip-path:polygon(25% 0,75% 0,100% 100%,0 100%)}

/* ticker */
.ticker{top:549px;height:102px;background:var(--blue-deep);text-align:center;color:#fff}
.ticker small{display:block;margin-top:32px;font-size:8px;letter-spacing:1px;color:#b7d9ee;text-transform:uppercase}
.ticker p{margin-top:8px;font-size:14px}

/* scale */
.scale{top:651px;height:354px}
.scale .section-title{margin-top:84px}
.verticals{position:absolute;top:185px;left:153px;width:892px;display:flex;justify-content:space-between}
.vertical{width:178px;text-align:center;border-right:1px solid var(--line);height:80px}
.vertical:last-child{border-right:0}
.vertical svg{display:block;margin:0 auto 12px}
.vertical span{font-size:10px;font-weight:700;text-transform:uppercase;color:var(--ink)}

/* clients */
.clients{top:1005px;height:268px;background:var(--blue);color:#fff;text-align:center}
.clients h2{margin-top:66px;font-size:20px;font-weight:600;line-height:36px;text-transform:uppercase;letter-spacing:.5px}
.client-row{position:absolute;top:168px;left:200px;width:800px;display:flex;justify-content:space-between;align-items:center}
.client{font-size:22px;font-weight:700;color:#fff}
.client.sm{font-size:14px}

/* why */
.why{top:1273px;height:415px}
.why .section-title{margin-top:80px}
.benefits{position:absolute;top:180px;left:198px;width:804px;display:flex;justify-content:space-between}
.benefit{width:210px;text-align:center}
.benefit svg{display:block;margin:0 auto 10px}
.benefit h4{font-size:10px;font-weight:700;text-transform:uppercase;margin-bottom:10px}
.benefit p{font-size:10.5px;line-height:16px;color:var(--muted)}

/* signup */
.signup{top:1688px;height:241px;background:var(--blue);text-align:center;color:#fff}
.signup h2{margin-top:48px;font-size:40px;font-weight:600;letter-spacing:1px}
.signup p{font-size:15px;color:#dff1fb;margin-top:2px}
.ghost{display:inline-block;margin-top:22px;width:225px;height:42px;border:1.5px solid #fff;border-radius:4px;line-height:39px;font-size:11px;font-weight:700;text-transform:uppercase}

/* features */
.features{top:1929px;height:804px}
.features .section-title{margin-top:68px;line-height:34px}
.tabs{position:absolute;top:193px;left:228px;width:817px;height:30px;border-bottom:1px solid var(--line)}
.tab{position:absolute;top:6px;font-size:10px;font-weight:600;text-transform:uppercase;transform:translateX(-50%);white-space:nowrap}
.tab.on{color:var(--blue)}
.tab.on::after{content:"";position:absolute;left:-6px;right:-6px;top:24px;height:3px;background:var(--blue)}
.features .lead{position:absolute;top:280px;width:100%;text-align:center;font-size:13px;color:var(--muted)}
.device{position:absolute;left:260px;top:335px;width:683px;height:400px;border-radius:14px 14px 4px 4px;background:linear-gradient(#3b3d40,#1d1e20)}
.device-screen{position:absolute;left:34px;top:22px;right:34px;bottom:48px;background:linear-gradient(#fafbfc,#e4ebf1)}
.device-base{position:absolute;left:-14px;right:-14px;bottom:-6px;height:22px;border-radius:0 0 40px 40px;background:linear-gradient(#d8dadd,#9ea2a7)}

/* faq */
.faq{top:2733px;height:450px;background:var(--mist)}
.faq .section-title{margin-top:44px}
.faq-list{position:absolute;left:161px;top:138px;width:410px;list-style:none}
.faq-list li{height:28px;border-bottom:1px solid #d8dbde;font-size:9px;font-weight:600;line-height:28px;text-transform:uppercase;color:#4a4d52;position:relative}
.faq-list li::after{content:"›";position:absolute;right:2px;font-size:14px;color:#8a8e93}
.faq-list li.on{color:var(--blue);border-bottom:2px solid var(--blue)}
.faq-text{position:absolute;left:664px;top:128px;width:388px;font-size:10px;line-height:16px;color:#55585d}
.dots{position:absolute;left:1075px;top:225px;display:flex;flex-direction:column;gap:6px}
.dots i{width:5px;height:5px;border-radius:50%;background:#c8ccd0;display:block}
.dots i.on{background:var(--blue)}

/* testimonials */
.reviews{top:3183px;height:487px;text-align:center}
.reviews .section-title{margin-top:68px}
.avatars{position:absolute;top:156px;left:0;width:100%;display:flex;justify-content:center;align-items:center;gap:10px}
.avatar{border-radius:50%;background:linear-gradient(135deg,#c9b7a6,#7a8088)}
.quote{position:absolute;top:236px;left:270px;width:660px;font-size:13.5px;font-style:italic;line-height:23px;color:#4a4d52}
.reviewer{position:absolute;top:378px;width:100%;font-size:12px;font-weight:700;color:var(--blue);text-transform:uppercase}
.role{position:absolute;top:402px;width:100%;font-size:8px;font-weight:600;color:var(--muted);text-transform:uppercase}
.arrow{position:absolute;top:282px}

/* footer */
.footer{top:3670px;height:348px;background:var(--night);color:#a9acb0}
.footer .brand{left:161px;top:66px;color:#fff}
.fcol{position:absolute;top:75px;font-size:9.5px;line-height:19px}
.fcol h5{font-size:10px;font-weight:700;color:#fff;text-transform:uppercase;margin-bottom:6px}
.fcol a{display:block;color:#a9acb0;text-decoration:none}
.fcol a.on{color:var(--blue)}
.lang{position:absolute;left:991px;top:75px;font-size:10px;line-height:19px;font-weight:600}
.lang .on{color:var(--blue)}
.fbar{position:absolute;left:153px;top:268px;width:892px;border-top:1px solid #3d3f42;padding-top:18px;font-size:9px;display:flex;justify-content:space-between}
.socials{display:flex;gap:12px}
.socials i{width:10px;height:10px;border-radius:50%;background:var(--blue);display:block}
</style>
</head>
<body>

<header class="wrap nav">
  <div class="brand">Textlyne</div>
  <nav class="menu">
    <span class="on">PRODUCTS ▾</span><span>APPS ▾</span><span>PRICES</span><span>BLOG</span><span>HELP CENTER</span>
  </nav>
  <div class="nav-btn" style="left:761px;width:139px">SCALE YOUR BUSINESS</div>
  <div class="nav-btn" style="left:906px;width:139px">BECOME A FREELANCER</div>
</header>

<section class="wrap hero" role="img" aria-label="Dimly lit office desk with a monitor and plant">
  <h1><b>Scale</b> your production of content and translation with our free platform.</h1>
  <div class="hero-col" style="left:161px">
    <h3>Business</h3>
    <p>Scale your online content. Free with your team or use our crowd.</p>
    <span class="cta">SIGN UP TO SCALE CONTENT</span>
  </div>
  <div class="hero-col" style="left:383px">
    <h3>Freelance</h3>
    <p>Freelance when you want. Earn with your language skills.</p>
    <span class="cta">SIGN UP TO FREELANCE</span>
  </div>
  <div class="video" role="img" aria-label="Desktop monitor showing the intro video">
    <svg class="video-play" width="22" height="22" viewBox="0 0 22 22"><circle cx="11" cy="11" r="10" fill="none" stroke="#fff" stroke-width="1.5"/><path d="M9 7l6 4-6 4z" fill="#fff"/></svg>
    <div class="video-label">Play video</div>
  </div>
  <div class="video-stand"></div>
</section>

<section class="wrap ticker">
  <small>Latest content from the crowd</small>
  <p><b>Mira</b> wrote the text <b>Golden Falcon Slot</b> in English 25 min ago</p>
</section>

<section class="wrap scale">
  <h2 class="section-title">What do you want to <span class="accent">scale?</span></h2>
  <div class="verticals">
    <div class="vertical">
      <svg width="48" height="48" viewBox="0 0 48 48" fill="none" stroke="#1ba3e6" stroke-width="2"><rect x="8" y="6" width="32" height="36" rx="3"/><rect x="13" y="12" width="22" height="14"/><path d="M18 19h12M14 33h6M28 33h6"/></svg>
      <span>iGaming</span>
    </div>
    <div class="vertical">
      <svg width="48" height="48" viewBox="0 0 48 48" fill="none" stroke="#1ba3e6" stroke-width="2"><rect x="5" y="8" width="38" height="26" rx="2"/><path d="M18 42h12M24 34v8M16 16h3l3 10h10l3-7H20"/></svg>
      <span>E-shop</span>
    </div>
    <div class="vertical">
      <svg width="48" height="48" viewBox="0 0 48 48" fill="none" stroke="#1ba3e6" stroke-width="2"><path d="M24 12a10 10 0 0 0-6 18v5h12v-5a10 10 0 0 0-6-18zM20 40h8M24 3v4M8 18h4M36 18h4M12 7l3 3M36 7l-3 3"/></svg>
      <span>New markets</span>
    </div>
    <div class="vertical">
      <svg width="48" height="48" viewBox="0 0 48 48" fill="none" stroke="#1ba3e6" stroke-width="2"><circle cx="24" cy="20" r="14"/><circle cx="24" cy="20" r="5"/><path d="M24 6v5M24 29v5M10 20h5M33 20h5M14 42h20"/></svg>
      <span>Agency</span>
    </div>
    <div class="vertical">
      <svg width="48" height="48" viewBox="0 0 48 48" fill="none" stroke="#1ba3e6" stroke-width="2"><rect x="6" y="8" width="22" height="16" rx="2"/><rect x="30" y="18" width="12" height="20" rx="2"/><path d="M4 40h26M10 28h14"/></svg>
      <span>Professional freelancing</span>
    </div>
  </div>
</section>

<section class="wrap clients">
  <h2>Helping some amazing companies grow<br>&amp; retain more costumers</h2>
  <div class="client-row">
    <span class="client">NORTHFIELD</span>
    <span class="client sm">Hemvik Group</span>
    <span class="client sm">VISITFLOW</span>
    <span class="client">Mr Clover</span>
    <span class="client sm">COOKVALE</span>
    <span class="client">Dorvin</span>
  </div>
</section>

<section class="wrap why">
  <h2 class="section-title">Why online businesses use <span class="accent">Textlyne?</span></h2>
  <div class="benefits">
    <div class="benefit">
      <svg width="44" height="44" viewBox="0 0 44 44" fill="none" stroke="#1ba3e6" stroke-width="2"><circle cx="22" cy="22" r="16"/><path d="M26 15h-6a3 3 0 0 0 0 6h4a3 3 0 0 1 0 6h-6M22 11v4M22 27v5"/></svg>
      <h4>50% cheaper</h4>
      <p>Online businesses using Textlyne save on average 50% on their internal and external costs for content and translation.</p>
    </div>
    <div class="benefit">
      <svg width="44" height="44" viewBox="0 0 44 44" fill="none" stroke="#1ba3e6" stroke-width="2"><circle cx="22" cy="22" r="16"/><circle cx="22" cy="22" r="9"/><circle cx="22" cy="22" r="2"/><path d="M22 22l16-12"/></svg>
      <h4>10x faster</h4>
      <p>With 1000s of freelance writers and translators Textlyne saves you tons of time.</p>
    </div>
    <div class="benefit">
      <svg width="44" height="44" viewBox="0 0 44 44" fill="none" stroke="#1ba3e6" stroke-width="2"><rect x="7" y="7" width="30" height="30" rx="3"/><path d="M13 30v-6M19 30v-10M25 30v-14M31 30v-8"/></svg>
      <h4>100% automated</h4>
      <p>Textlyne features 100% automated workflows including plagiarism scan and uploading texts to your site.</p>
    </div>
  </div>
</section>

<section class="wrap signup">
  <h2>SIGN UP NOW</h2>
  <p>Try for yourself, without charge</p>
  <span class="ghost">Get started – it's free!</span>
</section>

<section class="wrap features">
  <h2 class="section-title"><span class="accent">Textlyne</span> has features that will<br>revolutionize your <span class="accent">content writing</span></h2>
  <div class="tabs">
    <span class="tab on" style="left:72px">E-commerce content</span>
    <span class="tab" style="left:388px">Self-service content &amp; translations</span>
    <span class="tab" style="left:677px">iGaming content</span>
  </div>
  <p class="lead">We have expert solutions for multilingual eShops with more than 2000 products</p>
  <div class="device" role="img" aria-label="Laptop showing the project dashboard with order statistics">
    <div class="device-screen"></div>
    <div class="device-base"></div>
  </div>
</section>

<section class="wrap faq">
  <h2 class="section-title">Help &amp; FAQs</h2>
  <ul class="faq-list">
    <li>Why Textlyne, or even Textlyne for e-commerce?</li>
    <li class="on">Why e-commerce professionals love Textlyne?</li>
    <li>Connect your eShop or campaign to Textlyne now</li>
    <li>Textlyne mobile app – everything at your fingertips</li>
    <li>Why choose Textlyne?</li>
    <li>Textlyne gives you full control of your content strategy</li>
    <li>Self-service is the key to the future</li>
  </ul>
  <p class="faq-text">As an e-commerce professional, you have likely already figured out that the primary purpose of this landing page is to generate traffic for the focus keyword Textlyne, along with about 25 related long tail keywords. This is in direct competition with DocWriter. Well, you will love to hear that although an SEO specialist has done all the fun and core parts like strategy, the format of the content and the keyword research, all content that follows this paragraph and the rest of our landing pages have been written by the Textlyne crowd. After that, it is seamlessly uploaded upon approval (via mobile) through the Textlyne SitePress plugin.</p>
  <div class="dots"><i class="on"></i><i></i><i></i><i></i></div>
</section>

<section class="wrap reviews">
  <h2 class="section-title">What our <span class="accent">users</span> are saying</h2>
  <div class="avatars">
    <div class="avatar" style="width:36px;height:36px" role="img" aria-label="User portrait"></div>
    <div class="avatar" style="width:46px;height:46px" role="img" aria-label="Portrait of Elena"></div>
    <div class="avatar" style="width:36px;height:36px" role="img" aria-label="User portrait"></div>
  </div>
  <svg class="arrow" style="left:160px" width="14" height="22" viewBox="0 0 14 22"><path d="M11 3L4 11l7 8" fill="none" stroke="#8a8e93" stroke-width="2"/></svg>
  <svg class="arrow" style="left:1030px" width="14" height="22" viewBox="0 0 14 22"><path d="M3 3l7 8-7 8" fill="none" stroke="#8a8e93" stroke-width="2"/></svg>
  <p class="quote">After days at sea, I really enjoy sitting in some coffeeshop, opening my computer and connecting with other Textlyne writers and work with words instead of ropes and sails. And more! With Textlyne, I have discovered some corners of the digital world that I would otherwise have never visited. So, even while working I keep traveling.</p>
  <div class="reviewer">Elena</div>
  <div class="role">Freelance writer</div>
</section>

<footer class="wrap footer">
  <div class="brand">Textlyne</div>
  <div class="fcol" style="left:437px">
    <h5>Textlyne</h5>
    <a class="on">About Us</a><a>Team</a><a>Contact</a><a>Terms of Service</a><a>Privacy Policy</a><a>Imprint</a>
  </div>
  <div class="fcol" style="left:605px">
    <h5>Resources</h5>
    <a>Textlyne Affiliate</a><a>Careers</a><a>Developer Resources</a><a>Textlyne Workshops</a><a>Help</a>
  </div>
  <div class="fcol" style="left:772px">
    <h5>Contact</h5>
    <a>Textlyne B.V.</a><a>Havenkade 114</a><a>3011 AB Rotterdam</a><a>The Netherlands</a><a>Tel: +31 (0)20 555 0142</a><a>VAT: NL001234567B01</a>
  </div>
  <div class="lang"><div class="on">ENGLISH</div><div style="color:#fff">TÜRKÇE</div></div>
  <div class="fbar">
    <span>© 2018 Textlyne. All Rights Reserved.</span>
    <span class="socials"><i></i><i></i><i></i><i></i><i></i></span>
  </div>
</footer>

</body>
</html>
```